Video Sharing Site

UPDATE 2: Thanks to everyone who has submitted so far. I have decided to include 2nd and 3rd prizes are well, and I believe with a robust price. If you chose to participate, I will be working with the 2nd and 3rd prize winners also to use your selected designs to complete the rest of the webpages as specified in the brief.

-

UPDATE 1: The key is attractive, SOPHISTICATED yet roomy.

You are free to use any software package you like ie. Joomla, Drupal, Wordpress etc. We just need access to the HTML/CSS.

-

Hello everyone.

We require the HTML/CSS for a video sharing website. Our website is called ClipHarborly.com. Think of a unique logo. However this is not the main focus. I will try to give you as much info about the website design as I can:

# Home page:
- with categories in sidebar
- video listings eg. popular, most viewed, etc.
- perhaps make promoted videos stand out

# simple login page

# User Profile page
- user details
- user uploaded videos
- profile comments

# User Profile Edit page

# User Profile Inbox page
- mock messages

# Search page
- list of videos that match search
- number of results
- pagination
- etc.

# Video page
- page where we are watching a video
- related videos
- video comments
- video description
- ratings (thumbs up/down)
- views
- tags
- etc.

# Video Categories page
- list of a few categories eg. newest, most viewed, highest rated, etc.
- with 10-15 videos under each

# Video Upload page with form

# About Us
- with subcategories in sidebar (different design to video categories in home page sidebar)

# Contact Us

# Header
- as any website an attractive search bar should accompany the header
- quick shortlinks to logged-in user eg. (5) comments, (3) inbox, logout, etc.

# Footer
- should be thick so that it can accommodate links to more specific (mock) web pages.

# General
- please be sure to include advertising
- Don't be afraid to use bold colors.
- I will not be selecting designs that are overly dark
- be sure that any page where video thumbnails are shown are accompanied by video rating, number of views and author.
- think about loading times as well. Avoid the use of large graphics where possible.

########### HINT ##########
The first two designs that I pick will be two different types:
- colorful
- quite conservative. Plenty of white with light greys
###########################

Thanks everybody who submits!

2nd and 3rd prized now included!

Just to keep you all updated. I have made a few changes to the brief. Mostly just to make it easier for you to gauge what I'm after.

I have received enough designs with blue in it. Please submit designs where blue is not a main color. Thank you all!

Industry/Entity Type

Software

Requirements
Must have
• A sophisticated layout. It must look like a professional video sharing website.

```html
<!DOCTYPE html>
<html lang="en">
<head>
<meta charset="utf-8">
<title>ClipHarborly – About Us</title>
<link href="https://fonts.googleapis.com/css2?family=PT+Sans:wght@400;700&display=swap" rel="stylesheet">
<style>
:root{
  --page-bg:#e7e6e2;
  --red:#d51f38;
  --red-dark:#b5102a;
  --red-deep:#8f0a1f;
  --text-dark:#1d1d1d;
  --text-body:#8a8a8a;
  --accent:#c8102e;
  --grey-tab:#dcdcdc;
  --box-border:#d6d6d6;
  --item-bg:#e6e6e6;
  --footer-bg:#343434;
  --white:#ffffff;
}
*{margin:0;padding:0;box-sizing:border-box}
html,body{width:1200px;height:1145px;overflow:hidden}
body{background:var(--page-bg);font-family:"PT Sans",Arial,sans-serif;color:var(--text-dark);position:relative}
a{color:inherit;text-decoration:none}

.util-links{position:absolute;top:7px;left:572px;font-size:13px;display:flex;gap:12px;color:#333}
.util-links span.sep{color:#333}
.account-links{position:absolute;top:0;left:759px;width:340px;height:32px;background:var(--grey-tab);border-radius:0 0 4px 4px;display:flex;align-items:center;justify-content:center;gap:12px;font-size:13px;color:#333}

.site-header{position:absolute;top:43px;left:99px;width:1000px;height:122px;border-radius:4px 4px 0 0;
  background:linear-gradient(90deg,var(--red-dark) 0%,var(--red) 45%,var(--red-dark) 100%)}
.brand{position:absolute;left:20px;top:36px;display:flex;align-items:center;gap:14px}
.brand-dot{width:46px;height:46px;border-radius:50%;background:var(--white)}
.brand-name{font-size:30px;color:var(--white);font-weight:400;letter-spacing:-.5px}
.upload-tab{position:absolute;right:0;top:8px;width:211px;height:36px;background:var(--red-deep);border-radius:0 4px 0 4px;display:flex;align-items:center;gap:18px;padding-left:25px;color:var(--white);font-size:20px}
.upload-tab svg{display:block}
.search{position:absolute;left:787px;top:69px;width:199px;height:28px;background:var(--white);border-radius:3px;display:flex;align-items:center;justify-content:space-between;padding:0 6px 0 12px;font-size:12px;color:#aaa}

.main-nav{position:absolute;top:167px;left:99px;width:1000px;height:47px;background:linear-gradient(#f4f5f6,#cdd1d4);display:flex}
.main-nav a{height:47px;display:flex;align-items:center;justify-content:center;font-weight:700;font-size:15px;color:#222;border-right:1px solid #b9bdc0}
.main-nav a:last-child{border-right:none}

.content{position:absolute;top:214px;left:99px;width:1000px;height:835px;background:var(--white);box-shadow:0 0 6px rgba(0,0,0,.12)}
.breadcrumb{position:absolute;left:16px;top:31px;font-size:13px;color:#333}
.breadcrumb .raquo{margin:0 10px;color:#888}
.breadcrumb .current{color:var(--accent);text-decoration:underline}

.panel{position:absolute;background:var(--white);border:1px solid var(--box-border);border-radius:5px;overflow:hidden}
.panel-head{height:48px;background:linear-gradient(#f7f7f7,#e8e8e8);border-bottom:1px solid var(--box-border);display:flex;align-items:center;padding-left:18px;color:var(--accent);font-size:19px;font-weight:700;letter-spacing:.3px}
.about-panel{left:12px;top:76px;width:699px;height:623px}
.about-body{padding:24px 34px 0 24px}
.about-body h2{font-size:16px;font-weight:700;margin:0 0 12px;color:#1a1a1a}
.about-body h2.spaced{margin-top:30px;margin-bottom:25px}
.about-body p{font-size:12.6px;line-height:20px;color:var(--text-body);margin-bottom:9px}

.side-panel{left:719px;top:76px;width:267px;height:388px}
.side-list{list-style:none;padding:20px 18px 0}
.side-list li{height:41px;background:var(--item-bg);border-radius:3px;margin-bottom:10px;display:flex;align-items:center;padding-left:10px;gap:10px;font-weight:700;font-size:14.5px;color:#111}
.side-list li.active{color:var(--accent)}

.site-footer{position:absolute;top:1049px;left:0;width:1200px;height:96px;background:var(--footer-bg);color:var(--white);text-align:center}
.footer-links{padding-top:29px;font-size:12px;display:flex;justify-content:center;gap:9px}
.copyright{margin-top:10px;font-size:11px}
.copyright a{text-decoration:underline}
</style>
</head>
<body>

<nav class="util-links"><a href="#">Signup</a><span class="sep">|</span><a href="#">Help</a><span class="sep">|</span><a href="#">Browse</a></nav>
<nav class="account-links"><a href="#">My Account</a><span>|</span><a href="#">Inbox (2)</a><span>|</span><a href="#">Comments (3)</a><span>|</span><a href="#">Logout</a></nav>

<header class="site-header">
  <div class="brand"><span class="brand-dot"></span><span class="brand-name">ClipHarborly</span></div>
  <a class="upload-tab" href="#">
    <svg width="30" height="22" viewBox="0 0 30 22"><rect x="1" y="3" width="28" height="18" rx="4" fill="#2a2a2a"/><path d="M15 7l-6 6h4v5h4v-5h4z" fill="#d9d9d9"/></svg>
    Upload
  </a>
  <div class="search">Search videos
    <svg width="20" height="20" viewBox="0 0 20 20"><circle cx="8" cy="8" r="6" fill="none" stroke="#bbb" stroke-width="2.2"/><path d="M12.5 12.5l5.5 5.5" stroke="#bbb" stroke-width="3" stroke-linecap="round"/></svg>
  </div>
</header>

<nav class="main-nav">
  <a href="#" style="width:93px">Home</a>
  <a href="#" style="width:101px">Videos</a>
  <a href="#" style="width:115px">About Us</a>
  <a href="#" style="width:179px">Become a Member</a>
  <a href="#" style="width:145px">Latest Videos</a>
  <a href="#" style="width:143px">Most Viewed</a>
  <a href="#" style="width:130px">Contact Info</a>
</nav>

<main class="content">
  <div class="breadcrumb"><a href="#">Home</a><span class="raquo">»</span><a class="current" href="#">About Us</a></div>

  <section class="panel about-panel">
    <div class="panel-head">ABOUT US</div>
    <div class="about-body">
      <h2>WHO WE ARE</h2>
      <p>Sed ut perspiciatis unde omnis iste natus error sit voluptatem accusantium doloremque laudantium, totam rem aperiam, eaque ipsa quae ab illo inventore veritatis et quasi architecto beatae vitae dicta sunt explicabo. Nemo enim ipsam voluptatem quia voluptas sit aspernatur aut odit aut fugit.</p>
      <p>Sed ut perspiciatis unde omnis iste natus error sit voluptatem accusantium doloremque laudantium, totam rem aperiam, eaque ipsa quae ab illo inventore veritatis et quasi architecto beatae vitae dicta sunt explicabo. Nemo enim ipsam voluptatem quia voluptas sit aspernatur aut odit aut fugit.</p>
      <h2 class="spaced">WHY US ?</h2>
      <p>Sed ut perspiciatis unde omnis iste natus error sit voluptatem accusantium doloremque laudantium, totam rem aperiam, eaque ipsa quae ab illo inventore veritatis et quasi architecto beatae vitae dicta sunt explicabo. Nemo enim ipsam voluptatem quia voluptas sit aspernatur aut odit aut fugit.</p>
      <p>Sed ut perspiciatis unde omnis iste natus error sit voluptatem accusantium doloremque laudantium, totam rem aperiam, eaque ipsa quae ab illo inventore veritatis et quasi architecto beatae vitae dicta sunt explicabo. Nemo enim ipsam voluptatem quia voluptas sit aspernatur aut odit aut fugit.</p>
      <p>Sed ut perspiciatis unde omnis iste natus error sit voluptatem accusantium doloremque laudantium, totam rem aperiam, eaque ipsa quae ab illo inventore veritatis et quasi architecto beatae vitae dicta sunt explicabo. Nemo enim ipsam voluptatem quia voluptas sit aspernatur aut odit aut fugit.</p>
      <p>Sed ut perspiciatis unde omnis iste natus error sit voluptatem accusantium doloremque laudantium, totam rem aperiam, eaque ipsa quae ab illo inventore veritatis et quasi architecto beatae vitae dicta sunt explicabo. Nemo enim ipsam voluptatem quia voluptas sit aspernatur aut odit aut fugit.</p>
    </div>
  </section>

  <aside class="panel side-panel">
    <div class="panel-head">ABOUT CLIPHARBORLY</div>
    <ul class="side-list">
      <li class="active"><svg width="21" height="21" viewBox="0 0 21 21"><circle cx="10.5" cy="10.5" r="10" fill="#c8102e"/><path d="M5.5 10.5l3.5 3.5 6.5-7" fill="none" stroke="#fff" stroke-width="2.4"/></svg>Getting Started</li>
      <li><svg width="21" height="21" viewBox="0 0 21 21"><circle cx="10.5" cy="10.5" r="10" fill="#222"/><path d="M5.5 10.5l3.5 3.5 6.5-7" fill="none" stroke="#fff" stroke-width="2.4"/></svg>ClipHarborly Essentials</li>
      <li><svg width="21" height="21" viewBox="0 0 21 21"><circle cx="10.5" cy="10.5" r="10" fill="#222"/><path d="M5.5 10.5l3.5 3.5 6.5-7" fill="none" stroke="#fff" stroke-width="2.4"/></svg>Community Guidelines</li>
      <li><svg width="21" height="21" viewBox="0 0 21 21"><circle cx="10.5" cy="10.5" r="10" fill="#222"/><path d="M5.5 10.5l3.5 3.5 6.5-7" fill="none" stroke="#fff" stroke-width="2.4"/></svg>How it works</li>
      <li><svg width="21" height="21" viewBox="0 0 21 21"><circle cx="10.5" cy="10.5" r="10" fill="#222"/><path d="M5.5 10.5l3.5 3.5 6.5-7" fill="none" stroke="#fff" stroke-width="2.4"/></svg>Careers</li>
      <li><svg width="21" height="21" viewBox="0 0 21 21"><circle cx="10.5" cy="10.5" r="10" fill="#222"/><path d="M5.5 10.5l3.5 3.5 6.5-7" fill="none" stroke="#fff" stroke-width="2.4"/></svg>ClipHarborly Merchandise</li>
    </ul>
  </aside>
</main>

<footer class="site-footer">
  <nav class="footer-links"><a href="#">About us</a><span>|</span><a href="#">Contact us</a><span>|</span><a href="#">Terms</a><span>|</span><a href="#">Advertise</a><span>|</span><a href="#">Sitemap</a></nav>
  <p class="copyright">© 2011 <a href="#">ClipHarborly.com.</a> All rights reserved.</p>
</footer>

</body>
</html>
```